■ 依頼の目的/概要

ネットショップで購入者に送付する、「封筒」のデザインを依頼させて頂きます。

ショップURL http://www.pilmo-store.biz

■ 封筒デザインへの要望

女性向けショップなので、清潔感・きれいさを重視します。
ポストを覗いて当ショップのものだとわかるようなデザインが希望です。

■ 封筒の情報

記載
ショップ名(ロゴ) / 会社名 / 住所 / 電話/ URL

サイズ
角2 (240×332)  角6(162×229)

カラー
フルカラーでも、2色でも可

未定 デザイン決定後決めたく思いますが、デザインに対してのオススメがあればご提案ください。

■ 納品ファイルの希望

添付のテンプレートを使用ください。(イラストレーター)
※角2のみのテンプレなので、角6(162×229)はアレンジいただけると幸いです。

■ 進め方

弊社の希望するイメージに近い提案を1つ(場合によって複数)選択させて頂きます。
希望に近づけるために、修正要望を個別にさせて頂くこともあります。
コンペ方式のため、修正後に当選されない場合も、どうかご了承ください。

■ その他/注意点

選択させて頂いたデザインの著作権(財産権)等の扱いはBrivox利用規約に従い、弊社に譲渡をお願いします。フォントや画像素材などを利用する場合は上記利用用途に使用できることを確認し、第三者の知的財産権等に注意して下さい。
ファイルがUPされていなかったのでUPいたします。
多くの方にご提案いただきありがとうございました。

現在選定中ですので結果は今しばらくお待ちいただければと思います。

ご提案いただきました皆様、ありがとうございました。
■ 選んだ理由

女性らしいデザイン、カラー使いから決定させていただきました。

■ 提案者全員のお礼・コメント

数多くのご提案ありがとうございました。

選びかねた作品もございました。

また何かありましたらご依頼したく思います。

```html
<!DOCTYPE html>
<html lang="ja">
<head>
<meta charset="utf-8">
<title>pilmo 封筒デザイン</title>
<link rel="stylesheet" href="https://fonts.googleapis.com/css2?family=M+PLUS+Rounded+1c:wght@500;800&display=swap">
<style>
  :root {
    --leaf-green: #6cc51f;
    --flap-tint: #9bd95a;
    --paper: #ffffff;
    --outline: #9a9a9a;
    --accent-pink: #e8418c;
  }
  html, body {
    margin: 0;
    padding: 0;
    width: 822px;
    height: 1200px;
    overflow: hidden;
    background: var(--paper);
  }
  .envelope {
    position: relative;
    width: 822px;
    height: 1200px;
    font-family: "M PLUS Rounded 1c", sans-serif;
  }
  .envelope__body {
    position: absolute;
    left: 22px;
    top: 14px;
    width: 778px;
    height: 1150px;
    border: 2px solid var(--outline);
    box-sizing: border-box;
    background: var(--paper);
    overflow: hidden;
  }
  .envelope__flap {
    position: absolute;
    left: 0;
    top: 0;
    width: 100%;
    height: 100px;
    background: var(--leaf-green);
  }
  .envelope__flap-edge {
    position: absolute;
    left: 0;
    top: 100px;
    width: 100%;
    height: 16px;
    background: var(--flap-tint);
  }
  .flap-name {
    position: absolute;
    left: 50%;
    top: 28px;
    transform: translateX(-50%) rotate(180deg);
    color: var(--paper);
    font-weight: 800;
    font-size: 34px;
    letter-spacing: 1px;
  }
  .brand {
    position: absolute;
    left: 0;
    right: 0;
    top: 790px;
    display: flex;
    flex-direction: column;
    align-items: center;
  }
  .brand__row {
    display: flex;
    align-items: center;
    gap: 18px;
  }
  .brand__dot {
    width: 38px;
    height: 38px;
    border-radius: 50%;
    background: var(--accent-pink);
  }
  .brand__name {
    color: var(--leaf-green);
    font-weight: 800;
    font-size: 86px;
    line-height: 1;
  }
  .brand__url {
    margin-top: 14px;
    color: var(--leaf-green);
    font-weight: 500;
    font-size: 14px;
    letter-spacing: 0.5px;
  }
  .sender {
    position: absolute;
    left: 0;
    right: 0;
    top: 1105px;
    text-align: center;
    color: var(--leaf-green);
    font-weight: 500;
    font-size: 13px;
    letter-spacing: 0.3px;
  }
  .sender span + span { margin-left: 14px; }
</style>
</head>
<body>
  <div class="envelope">
    <div class="envelope__body">
      <div class="envelope__flap">
        <div class="flap-name">pilmo</div>
      </div>
      <div class="envelope__flap-edge"></div>

      <div class="brand">
        <div class="brand__row">
          <div class="brand__dot"></div>
          <div class="brand__name">pilmo</div>
        </div>
        <div class="brand__url">http://www.pilmo-store.biz</div>
      </div>

      <div class="sender">
        <span>株式会社 ピルモ</span>
        <span>〒150-0042 東京都港区南青山 2-4-8</span>
        <span>TEL:03-5412-7780 FAX:03-5412-7781</span>
      </div>
    </div>
  </div>
</body>
</html>
```